Brookfarrow Osteopathy and dry needling business card

Business card for Brookfarrow Osteopathy and Dry Needling.

Industry/Entity Type

Health

Contact Information for Business Card

I do not have a phone number yet. I also do not have an email address yet. The physical address is: 48 Lower Crane Street Brookfarrow The website is: www.brookfarrowosteosteopathy.example My details are: Dr Martin Pellowe, Osteopath (B.Clin.Sci (Ost) M.Ost BSC ECON (Hons)

Colors
0094D4
00A9DD
6FCCEA
C7EBF8
E9F6FB

Requirements
Must have
• logo on the back
Nice to have
• Maybe a space for me to write an appointment time and date on the card.

```html
<!DOCTYPE html>
<html lang="en">
<head>
<meta charset="utf-8">
<title>Brookfarrow Osteopathy and Dry Needling – Business Card</title>
<link rel="stylesheet" href="https://fonts.googleapis.com/css2?family=Arimo:wght@400;700&display=swap">
<style>
  :root {
    --backdrop: #999999;
    --card: #1f1f1f;
    --text: #ffffff;
    --orange: #f39a2b;
    --blue: #0094d4;
    --blue-bright: #00a9dd;
    --emboss: #3a3a3a;
    --emboss-text: #4a4a4a;
  }
  * { margin: 0; padding: 0; box-sizing: border-box; }
  html, body { width: 1200px; height: 1059px; overflow: hidden; }
  body {
    background: var(--backdrop);
    font-family: "Arimo", Arial, sans-serif;
    position: relative;
  }
  .card {
    position: absolute;
    width: 690px;
    height: 392px;
    background: var(--card);
    border-radius: 22px;
  }
  .card--front { left: 256px; top: 89px; }
  .card--back { left: 254px; top: 569px; }

  .brand-mark {
    position: absolute;
    border-radius: 50%;
    display: flex;
    align-items: center;
    justify-content: center;
    text-align: center;
    font-weight: 700;
  }
  .card--front .brand-mark {
    left: 101px; top: 108px;
    width: 176px; height: 176px;
    border: 2px solid var(--blue-bright);
    color: var(--blue-bright);
    font-size: 17px;
    line-height: 1.25;
    padding: 20px;
  }
  .card--back .brand-mark {
    left: 228px; top: 81px;
    width: 232px; height: 232px;
    border: 2px solid var(--emboss);
    color: var(--emboss-text);
    font-size: 22px;
    line-height: 1.25;
    padding: 28px;
  }

  .divider {
    position: absolute;
    left: 309px; top: 111px;
    width: 1px; height: 170px;
    background: linear-gradient(to bottom, transparent, var(--orange) 25%, var(--orange) 75%, transparent);
    opacity: 0.7;
  }
  .details {
    position: absolute;
    left: 341px; top: 120px;
    color: var(--text);
  }
  .person-name {
    font-size: 23px;
    font-weight: 700;
    letter-spacing: 0.2px;
    line-height: 1;
  }
  .person-name .first { color: var(--orange); }
  .person-name .last { color: var(--blue); }
  .credentials {
    margin-top: 6px;
    font-size: 17.5px;
    line-height: 21px;
  }
  .contact { margin-top: 24px; list-style: none; font-size: 17px; }
  .contact li {
    display: flex;
    align-items: center;
    gap: 7px;
    height: 22px;
    margin-bottom: 7px;
  }
  .contact svg { width: 14px; height: 14px; flex: none; }
</style>
</head>
<body>
  <section class="card card--front">
    <div class="brand-mark">Brookfarrow Osteopathy and Dry Needling</div>
    <div class="divider"></div>
    <div class="details">
      <h1 class="person-name"><span class="first">DR MARTIN</span> <span class="last">PELLOWE</span></h1>
      <p class="credentials">Osteopath (B.Clin.Sci (Ost)<br>M.Ost BSC ECON (Hons)</p>
      <ul class="contact">
        <li>
          <svg viewBox="0 0 16 16" aria-hidden="true" fill="none" stroke="#0094d4" stroke-width="1.3">
            <circle cx="8" cy="8" r="6.5"/>
            <ellipse cx="8" cy="8" rx="3" ry="6.5"/>
            <line x1="1.5" y1="8" x2="14.5" y2="8"/>
            <line x1="2.5" y1="4.8" x2="13.5" y2="4.8"/>
            <line x1="2.5" y1="11.2" x2="13.5" y2="11.2"/>
          </svg>
          <span>www.brookfarrowosteosteopathy.example</span>
        </li>
        <li>
          <svg viewBox="0 0 16 16" aria-hidden="true">
            <path d="M8 0.5a5.5 5.5 0 0 0-5.5 5.5c0 4 5.5 9.5 5.5 9.5s5.5-5.5 5.5-9.5A5.5 5.5 0 0 0 8 0.5z" fill="#0094d4"/>
            <circle cx="8" cy="6" r="2.1" fill="#1f1f1f"/>
          </svg>
          <span>48 Lower Crane Street Brookfarrow</span>
        </li>
      </ul>
    </div>
  </section>

  <section class="card card--back">
    <div class="brand-mark">Brookfarrow Osteopathy and Dry Needling</div>
  </section>
</body>
</html>
```